Business Card Design for Animal Clinic

We are seeking a two sided business card design. The primary side should include our logo (provided in AI and EPS files) address, phone, website, and if possible "Follow Us" with icons for Facebook, Google+, and Twitter.

The back of the card needs to included space for appointment reminders.

Company Name:
Calderbrook Animal Clinic

Doctor Name:
To be provided to winner

Adress:
To be provided to winner

Phone:
to be provided to winner

Website:
www.calderbrookanimalclinic.com

```html
<!DOCTYPE html>
<html lang="en">
<head>
<meta charset="utf-8">
<title>Calderbrook Animal Clinic – Business Card</title>
<link rel="stylesheet" href="https://fonts.googleapis.com/css2?family=Didact+Gothic&family=Josefin+Slab:wght@400&family=Nunito+Sans:wght@800&display=swap">
<style>
  :root {
    --clinic-red: #a11d21;
    --stripe-pink: #d4898c;
    --label-pink: #cf8c8f;
    --card-white: #ffffff;
    --backdrop: #e9e6e2;
  }
  * { box-sizing: border-box; margin: 0; padding: 0; }
  html, body { width: 1200px; height: 1000px; overflow: hidden; }
  body {
    background: var(--backdrop);
    position: relative;
    font-family: "Didact Gothic", "Century Gothic", sans-serif;
  }
  .card {
    position: absolute;
    width: 740px;
    height: 420px;
    background: var(--card-white);
    border-radius: 36px;
    overflow: hidden;
    box-shadow: 0 10px 30px rgba(0,0,0,0.18);
  }
  .card--front { left: 70px; top: 50px; }
  .card--back { left: 390px; top: 530px; }

  /* front */
  .brand {
    position: absolute;
    left: 0; right: 0; top: 70px;
    display: flex; align-items: center; justify-content: center; gap: 18px;
  }
  .brand__dot { width: 22px; height: 22px; border-radius: 50%; background: var(--clinic-red); }
  .brand__name {
    font-family: "Josefin Slab", serif;
    font-weight: 400;
    font-size: 50px;
    letter-spacing: 2px;
    color: var(--clinic-red);
    text-transform: uppercase;
    line-height: 1.1;
    text-align: center;
  }
  .phone {
    position: absolute; right: 50px; top: 248px;
    display: flex; align-items: center; gap: 8px;
    font-size: 28px; color: var(--clinic-red); letter-spacing: 1px;
  }
  .doctor-name {
    position: absolute; left: 40px; top: 298px;
    font-family: "Nunito Sans", sans-serif; font-weight: 800;
    font-size: 30px; color: var(--clinic-red);
  }
  .band {
    position: absolute; left: 0; right: 0; bottom: 0;
    background: var(--clinic-red);
    border-top: 9px solid var(--stripe-pink);
  }
  .card--front .band { height: 78px; }
  .website {
    position: absolute; left: 0; right: 0; top: 16px;
    text-align: center; font-size: 28px; color: var(--card-white); letter-spacing: 0.5px;
  }

  /* back */
  .appointment__title {
    position: absolute; left: 0; right: 0; top: 26px;
    text-align: center; font-size: 34px; color: var(--clinic-red);
  }
  .appointment__field {
    position: absolute; left: 110px; right: 160px;
    display: flex; align-items: flex-end; gap: 40px;
  }
  .appointment__field--date { top: 78px; }
  .appointment__field--time { top: 144px; }
  .field__label { width: 70px; font-size: 28px; color: var(--label-pink); }
  .field__line { flex: 1; border-bottom: 2px solid var(--clinic-red); margin-bottom: 4px; }
  .card--back .band { height: 212px; }
  .clinic-title {
    position: absolute; left: 0; right: 0; top: 28px;
    text-align: center; font-family: "Nunito Sans", sans-serif; font-weight: 800;
    font-size: 32px; color: var(--label-pink);
  }
  .address { position: absolute; left: 40px; top: 82px; color: var(--card-white); font-size: 22px; line-height: 1.3; }
  .address__label { color: var(--label-pink); font-size: 28px; }
  .follow { position: absolute; right: 60px; top: 118px; text-align: center; }
  .follow__label { color: var(--card-white); font-size: 26px; }
  .follow__icons { display: flex; gap: 18px; justify-content: center; margin-top: 22px; }
  .follow__icon { width: 30px; height: 30px; border-radius: 6px; background: var(--label-pink); }
</style>
</head>
<body>
  <section class="card card--front" aria-label="Card front">
    <div class="brand">
      <span class="brand__dot"></span>
      <span class="brand__name">Calderbrook<br>Animal Clinic</span>
    </div>
    <div class="phone">
      <span>07185526034</span>
      <svg width="16" height="24" viewBox="0 0 16 24" aria-hidden="true">
        <rect x="2" y="1" width="12" height="22" rx="2" fill="none" stroke="#a11d21" stroke-width="2.5"/>
        <line x1="6" y1="19" x2="10" y2="19" stroke="#a11d21" stroke-width="2"/>
      </svg>
    </div>
    <div class="doctor-name">Doctor Name</div>
    <div class="band">
      <div class="website">www.calderbrookanimalclinic.com</div>
    </div>
  </section>

  <section class="card card--back" aria-label="Card back">
    <div class="appointment__title">Appointment</div>
    <div class="appointment__field appointment__field--date">
      <span class="field__label">Date</span><span class="field__line"></span>
    </div>
    <div class="appointment__field appointment__field--time">
      <span class="field__label">Time</span><span class="field__line"></span>
    </div>
    <div class="band">
      <div class="clinic-title">Calderbrook Animal Clinic</div>
      <div class="address">
        <div class="address__label">Address</div>
        <div>#413 dummytxt</div>
        <div>Dummytxt dummytxt</div>
      </div>
      <div class="follow">
        <div class="follow__label">"Follow Us"</div>
        <div class="follow__icons">
          <span class="follow__icon" role="img" aria-label="Social network link"></span>
          <span class="follow__icon" role="img" aria-label="Social network link"></span>
          <span class="follow__icon" role="img" aria-label="Social network link"></span>
        </div>
      </div>
    </div>
  </section>
</body>
</html>
```